Solo consultant in research/analytics/data science space needs new business card

I need a new business card to promote my solo business as creative problem solver and consultant. I work on business projects for sales and market research and analytics, customer/market insights, and data science. I provide clients data-informed insights and ideas to enhance their businesses. My initial tagline: 'Make your data work for YOU.'

People should hire me because of my diverse background. Because of my Ph.D. in Political Science I have a strong background in research and analytics, project design and management, and communications skills. With my experience as a marketing analyst, a volunteer on non-profit projects, and currently as research consultant I have worked on projects within various industries. I also have a taste for improvisation so I enjoy thinking creatively and appreciate design thinking.

As an introduction to my background: Clients might want to hire me for many types of projects. Clients might wish to understand who their best customers are and how to characterize them. Maybe clients want to know how their customers feel about a certain product or service. Clients might want to know more about their local market area and overall industry. Clients might want to know whether their marketing programs are effective or else what drives their sales revenue. Perhaps clients want to use their data to create something useful for themselves or their customers.

One client hired me to help them decide whether to expand their services to newer customers. I gathered and analyzed information about the local area – the characteristics of people living there as well as the client’s competitors – and described trends and implications. The client was very pleased with the results and submitted them to superiors for approval to move forward.

For another client – who was looking to purchase a house in a metropolitan area – I gathered population and school data about the area. With this, I created an interactive mapping tool so they could zoom in on neighborhoods and learn more about them before they selected a neighborhood to purchase a house. They were happy with the results of my work.

When I worked as a marketing analyst for a consulting firm, a Vice President of Marketing hired us to discover whether or not the company’s marketing programs (i.e. coupons and discounts) were effective. I analyzed their data and our team discovered their marketing was indeed effective. He was very happy and used this to justify their programs to the Finance department (who thought such programs lost revenue).

- Mark Dennis Hollow, Ph.D.

Target Market(s)

Future clients and employers. The most immediate target markets will be other service providers such as consulting companies, marketing firms and ad agencies. I will also use this for meeting with clients in various industries.

Industry/Entity Type

Consulting

Contact Information for Business Card

Since it is my first real business card as a solo practitioner, I want to make an excellent first impression. I want this useful in case someone hires me to work on projects or else hire me to work within a firm or company. The card should convey competence and some creativity while also being neither stuffy nor a data geek.

Colors

Designer to choose colors to be used in the design.

Requirements
Nice to have
• Attached are the starting efforts at the card to add some color. It will be nice to use my name and descriptors on one side and tagline on the other. If anyone has better ideas, I will love to see them!

```html
<!DOCTYPE html>
<html lang="en">
<head>
<meta charset="utf-8">
<title>Mark Dennis Hollow, Ph.D. — Business Card</title>
<link rel="stylesheet" href="https://fonts.googleapis.com/css2?family=Mulish:wght@700;800&family=Montserrat:wght@500&family=Lato:wght@400&display=swap">
<style>
  :root {
    --backdrop: #2a2a2a;
    --card-black: #1c1c1c;
    --card-white: #ffffff;
    --accent-red: #e3262b;
    --ink: #1a1a1a;
    --divider: #3a3a3a;
    --band-text: #ffffff;
  }
  * { margin: 0; padding: 0; box-sizing: border-box; }
  html, body {
    width: 1200px; height: 895px; overflow: hidden;
    background: var(--backdrop);
  }
  .canvas {
    position: relative; width: 1200px; height: 895px;
    display: flex; flex-direction: column; align-items: center; justify-content: center;
    gap: 56px;
  }
  .card {
    position: relative; width: 620px; height: 354px;
    box-shadow: 0 10px 30px rgba(0,0,0,.45);
    overflow: hidden;
  }
  /* Front: tagline */
  .card--front {
    background: var(--card-black);
    display: flex; align-items: center; justify-content: center;
  }
  .tagline {
    font-family: "Mulish", sans-serif; font-weight: 800;
    font-size: 46px; line-height: 1.02; letter-spacing: .5px;
    color: #fff; text-align: left;
  }
  .tagline__accent { color: var(--accent-red); }
  .tagline__line2 { display: block; padding-left: 150px; color: var(--accent-red); }

  /* Back: identity */
  .card--back { background: var(--card-white); }
  .identity {
    position: absolute; right: 255px; top: 118px; text-align: right;
  }
  .identity__name {
    font-family: "Montserrat", sans-serif; font-weight: 500;
    font-size: 24px; color: var(--accent-red); letter-spacing: -.3px;
    white-space: nowrap;
  }
  .identity__role {
    font-family: "Lato", sans-serif; font-size: 22px; color: var(--ink);
    margin-top: 2px;
  }
  .divider {
    position: absolute; left: 385px; top: 88px; width: 1px; height: 128px;
    background: var(--divider);
  }
  .contacts {
    position: absolute; left: 400px; top: 84px; list-style: none;
    font-family: "Lato", sans-serif; font-size: 13px; color: var(--ink);
  }
  .contacts__item { display: flex; align-items: center; height: 26px; gap: 9px; }
  .contacts__icon { width: 13px; height: 13px; flex: none; }
  .band {
    position: absolute; left: 0; right: 0; bottom: 0; height: 72px;
    background: var(--card-black);
    display: flex; align-items: center; justify-content: center;
  }
  .band__services {
    font-family: "Lato", sans-serif; font-size: 15px; color: var(--band-text);
    letter-spacing: .6px;
  }
</style>
</head>
<body>
<main class="canvas">
  <section class="card card--front">
    <p class="tagline">Make Data <span class="tagline__accent">Work</span><span class="tagline__line2">For YOU.</span></p>
  </section>

  <section class="card card--back">
    <div class="identity">
      <p class="identity__name">MARK DENNIS HOLLOW, Ph.D.</p>
      <p class="identity__role">Consultant</p>
    </div>
    <div class="divider"></div>
    <ul class="contacts">
      <li class="contacts__item">
        <svg class="contacts__icon" viewBox="0 0 12 12"><path d="M6 0.5a4 4 0 0 0-4 4c0 3 4 7 4 7s4-4 4-7a4 4 0 0 0-4-4z" fill="var(--accent-red)"/><circle cx="6" cy="4.5" r="1.4" fill="#fff"/></svg>
        Braga, PT
      </li>
      <li class="contacts__item">
        <svg class="contacts__icon" viewBox="0 0 12 12"><rect x="3" y="0.8" width="6" height="10.4" rx="1" fill="none" stroke="var(--accent-red)" stroke-width="1.3"/><circle cx="6" cy="9.3" r=".6" fill="var(--accent-red)"/></svg>
        +351 910 246 813
      </li>
      <li class="contacts__item">
        <svg class="contacts__icon" viewBox="0 0 12 12"><rect x="0.5" y="2.5" width="11" height="7.5" fill="var(--accent-red)"/><path d="M0.8 2.8 6 6.8l5.2-4" fill="none" stroke="#fff" stroke-width="1"/></svg>
        mdhollow70@mailbox.com
      </li>
      <li class="contacts__item">
        <svg class="contacts__icon" viewBox="0 0 12 12"><circle cx="6" cy="6" r="5" fill="none" stroke="var(--accent-red)" stroke-width="1.2"/><ellipse cx="6" cy="6" rx="2.2" ry="5" fill="none" stroke="var(--accent-red)" stroke-width="1"/><path d="M1 6h10" stroke="var(--accent-red)" stroke-width="1"/></svg>
        www.markdennishollow.com
      </li>
      <li class="contacts__item">
        <svg class="contacts__icon" viewBox="0 0 12 12"><circle cx="6" cy="6" r="5" fill="var(--accent-red)"/></svg>
        @MarkHollow70
      </li>
    </ul>
    <div class="band">
      <p class="band__services">Predictive Analytics - Business Intelligence - Data Science</p>
    </div>
  </section>
</main>
</body>
</html>
```